Velvet Comet Cocoa Slab - ComettaSlabs.com

Create chocolate bar packaging. I would like the packaging to have a wizard hat or wizard with hat on on the packaging. Packaging should be a matte finish with a glossy Wizard hat or wizard with hat on the packaging. The background should have little wizard hats or mushrooms that are imbedded into the matte finish that reflect when you move the packaging. Colors should be Black, dark purple, purple, blue, dark blue, white.

Target Market(s)

Mushroom Consumers

Industry/Entity Type

Mushroom Chocolates

Font styles to use
Serif
Sans Serif

Colors
0054AA
0677BA
7BADD7
CADEEF
E8F1F8
0094D4
00A9DD
6FCCEA
C7EBF8
E9F6FB
A7469A
B969AE
D3A5CF
EDDBEB
F8F0F9
6B429C
8869AF
B7A5CE
E3DAEB
F3F0F8

Requirements
Must have
• Wizard Hat
Nice to have
• Reflective small mushrooms or wizard hats in the matte background
Should not have
• to many colors

```html
<!DOCTYPE html>
<html lang="en">
<head>
<meta charset="utf-8">
<title>Velvet Comet Cocoa Slab – Wrapper</title>
<link rel="stylesheet" href="https://fonts.googleapis.com/css2?family=Oswald:wght@300;400&family=Kalam:wght@400&display=swap">
<style>
  :root {
    --stage: #f1f1f3;
    --wrap-deep: #140c22;
    --wrap-mid: #2a1c44;
    --wrap-glow: #3d2a60;
    --crimp: #1d1430;
    --band-dark: #0d0816;
    --ink-white: #f3f0f8;
    --ink-lilac: #d3a5cf;
    --ink-lavender: #b7a5ce;
    --art-blue: #0054aa;
    --art-dark: #0c0a14;
    --art-warm: #c7562a;
  }
  * { margin: 0; padding: 0; box-sizing: border-box; }
  html, body {
    width: 1200px; height: 900px; overflow: hidden;
    background: var(--stage);
  }
  .wrapper {
    position: absolute; left: 380px; top: 40px;
    width: 440px; height: 820px;
  }
  .wrapper-shape { position: absolute; inset: 0; }
  .sheen-pattern {
    position: absolute; left: 20px; top: 80px; width: 400px; height: 600px;
    background: radial-gradient(ellipse at 50% 45%, rgba(183,165,206,0.10), rgba(183,165,206,0) 70%);
  }
  .wrapper-content {
    position: absolute; left: 0; right: 0; top: 0; height: 680px;
    display: flex; flex-direction: column; align-items: center;
    text-align: center;
  }
  .hat-art {
    margin-top: 112px;
    width: 240px; height: 190px;
    border-radius: 10px;
    background: radial-gradient(ellipse at 45% 40%, var(--art-blue) 0%, #1a2a5c 45%, #3a1f3a 75%, var(--art-warm) 130%);
    opacity: 0.85;
  }
  .brand-name {
    margin-top: 30px;
    font-family: 'Oswald', sans-serif; font-weight: 400;
    font-size: 50px; line-height: 1.08; letter-spacing: 1px;
    color: var(--ink-white); text-transform: uppercase;
  }
  .flavor {
    margin-top: 30px;
    font-family: 'Kalam', cursive; font-size: 36px; line-height: 1;
    color: var(--ink-lilac);
  }
  .variant {
    margin-top: 12px;
    font-family: 'Oswald', sans-serif; font-weight: 300;
    font-size: 32px; letter-spacing: 2px;
    color: var(--ink-lavender);
  }
  .dose-line {
    position: absolute; left: 0; right: 0; top: 680px; height: 66px;
    display: flex; align-items: center; justify-content: center;
    font-family: 'Oswald', sans-serif; font-weight: 300;
    font-size: 14px; letter-spacing: 0.6px;
    color: var(--ink-white); text-transform: uppercase;
  }
</style>
</head>
<body>
  <div class="wrapper">
    <svg class="wrapper-shape" width="440" height="820" viewBox="0 0 440 820" aria-hidden="true">
      <defs>
        <pattern id="teeth-top" width="20" height="10" patternUnits="userSpaceOnUse">
          <polygon points="0,10 10,0 20,10" fill="var(--crimp)"/>
        </pattern>
        <pattern id="teeth-bottom" width="20" height="10" patternUnits="userSpaceOnUse">
          <polygon points="0,0 10,10 20,0" fill="var(--crimp)"/>
        </pattern>
        <radialGradient id="body-fill" cx="50%" cy="48%" r="65%">
          <stop offset="0" stop-color="var(--wrap-glow)"/>
          <stop offset="0.6" stop-color="var(--wrap-mid)"/>
          <stop offset="1" stop-color="var(--wrap-deep)"/>
        </radialGradient>
      </defs>
      <rect x="0" y="0" width="440" height="10" fill="url(#teeth-top)"/>
      <rect x="0" y="10" width="440" height="64" fill="var(--crimp)"/>
      <rect x="0" y="74" width="440" height="606" fill="url(#body-fill)"/>
      <rect x="0" y="680" width="440" height="66" fill="var(--band-dark)"/>
      <rect x="0" y="746" width="440" height="64" fill="var(--crimp)"/>
      <rect x="0" y="810" width="440" height="10" fill="url(#teeth-bottom)"/>
      <line x1="0" y1="74" x2="440" y2="74" stroke="var(--band-dark)" stroke-width="2"/>
      <line x1="0" y1="746" x2="440" y2="746" stroke="var(--band-dark)" stroke-width="2"/>
    </svg>
    <div class="sheen-pattern" role="img" aria-label="Faint scattered mushroom shapes embossed in the matte background"></div>
    <div class="wrapper-content">
      <div class="hat-art" role="img" aria-label="Glossy illustration of a pointed wizard hat with blue folds, orange band and gold buckle"></div>
      <h1 class="brand-name">Velvet Comet<br>Cocoa Slab</h1>
      <p class="flavor">cookies &amp; cream</p>
      <p class="variant">- ENIGMA -</p>
    </div>
    <p class="dose-line">3.5 grams of comet magic in every bar</p>
  </div>
</body>
</html>
```